Cool modern, tech Business card design

Looking for a new business card design for our Managed IT Services company. We would like 2 sides, with the logo one one side horizontally and then the information on the back in either vertical or horizontal. We want our colors from the logo incorporated but also would like to see the color gray in there as well.

Target Market(s)

IT, Information Technology, Tech, Service

Industry/Entity Type

It Service

Contact Information for Business Card

Pavel Lind
Managing Partner
(P)742-318-6650 ext xxx
(F)742-318-6651
www.qelvantrixo.com

Font styles to use
Sans Serif

Colors
959595
000000
ec1f27

Requirements
Must have
• Logo on one side with some nice design or pattern
• Information on back in either vertical or horizontal format
Nice to have
• For it to look cool, tech, modern, stand out.

```html
<!DOCTYPE html>
<html lang="en">
<head>
<meta charset="UTF-8">
<title>Qelvantrixo Business Card</title>
<link rel="stylesheet" href="https://fonts.googleapis.com/css2?family=Ubuntu:wght@400;500&display=swap">
<style>
  :root {
    --brand-red: #a91e2b;
    --brand-red-dark: #961a26;
    --ink: #1a1a1a;
    --paper: #f4f4f4;
    --backdrop: #b4b4b4;
    --white: #ffffff;
  }
  * { box-sizing: border-box; margin: 0; padding: 0; }
  html, body {
    width: 1200px;
    height: 576px;
    overflow: hidden;
    background: var(--backdrop);
    font-family: "Ubuntu", sans-serif;
  }
  .card {
    position: absolute;
    top: 140px;
    width: 484px;
    height: 292px;
    border-radius: 14px;
    overflow: hidden;
    box-shadow: 0 3px 6px rgba(0, 0, 0, 0.25);
  }
  .card-front {
    left: 82px;
    background: linear-gradient(180deg, var(--brand-red) 0%, var(--brand-red-dark) 100%);
  }
  .front-wordmark {
    position: absolute;
    left: 0;
    right: 0;
    top: 118px;
    display: flex;
    justify-content: center;
    align-items: center;
    gap: 10px;
    color: var(--white);
    font-size: 38px;
    font-weight: 500;
    letter-spacing: 0.5px;
  }
  .wordmark-square {
    width: 16px;
    height: 16px;
    background: var(--white);
  }
  .card-back {
    left: 602px;
    background: var(--paper);
  }
  .back-wordmark {
    position: absolute;
    left: 30px;
    top: 125px;
    display: flex;
    align-items: center;
    gap: 8px;
    color: var(--ink);
    font-size: 28px;
    font-weight: 500;
  }
  .back-wordmark .wordmark-square {
    width: 13px;
    height: 13px;
    background: var(--brand-red);
  }
  .contact {
    position: absolute;
    left: 276px;
    top: 56px;
    color: var(--ink);
    font-size: 12.5px;
    line-height: 16.5px;
  }
  .contact-name {
    color: var(--brand-red);
    font-size: 21px;
    font-weight: 500;
    line-height: 24px;
  }
  .contact-title { margin-top: 2px; }
  .contact-address { margin-top: 15px; }
  .contact-lines { margin-top: 7px; list-style: none; }
  .contact-lines li {
    display: flex;
    align-items: center;
    gap: 9px;
    height: 17px;
  }
  .contact-icon { width: 11px; height: 11px; fill: var(--brand-red); }
  .footer-strip {
    position: absolute;
    left: 0;
    bottom: 0;
    width: 260px;
    height: 12px;
    background: var(--ink);
  }
  .footer-band {
    position: absolute;
    right: 0;
    bottom: 0;
    width: 255px;
    height: 36px;
    background: var(--brand-red);
    clip-path: polygon(18px 0, 100% 0, 100% 100%, 0 100%);
  }
  .footer-web {
    position: absolute;
    left: 276px;
    bottom: 11px;
    color: var(--white);
    font-size: 12px;
  }
</style>
</head>
<body>
  <section class="card card-front">
    <div class="front-wordmark">
      <span>qelvantrixo</span>
      <span class="wordmark-square"></span>
    </div>
  </section>

  <section class="card card-back">
    <div class="back-wordmark">
      <span>qelvantrixo</span>
      <span class="wordmark-square"></span>
    </div>

    <div class="contact">
      <p class="contact-name">Pavel Lind</p>
      <p class="contact-title">Managing Partner</p>
      <p class="contact-address">214 Harlow Lane Brookfield,<br>Ohio 44403</p>
      <ul class="contact-lines">
        <li>
          <svg class="contact-icon" viewBox="0 0 12 12" aria-hidden="true"><path d="M1 4c0-2 2-3 5-3s5 1 5 3v1H8V4H4v1H1z M2 6h8l1 5H1z"/></svg>
          742-318-6650 ext xxx
        </li>
        <li>
          <svg class="contact-icon" viewBox="0 0 12 12" aria-hidden="true"><path d="M1 4c0-2 2-3 5-3s5 1 5 3v1H8V4H4v1H1z M2 6h8l1 5H1z"/></svg>
          742-318-6651
        </li>
        <li>
          <svg class="contact-icon" viewBox="0 0 12 12" aria-hidden="true"><path d="M1 3h10v7H1z" /><path d="M1 3l5 4 5-4" fill="none" stroke="#f4f4f4" stroke-width="1"/></svg>
          pavel@qelvantrixo.com
        </li>
      </ul>
    </div>

    <div class="footer-strip"></div>
    <div class="footer-band"></div>
    <p class="footer-web">www.qelvantrixo.com</p>
  </section>
</body>
</html>
```